Energy Efficiency Case Study for energy reduction

We need a case study template for energy efficiency projects/studies we have done for other companies to use on our website and to new prospective clients in an email campaign. We create added value to our clients with our structured + focused approach. We are a small dedicated group of energy experts led by 2013 International Energy Manager of the year Gerald Phinney. We would like to tell the story of the project, highlighting the added value we were able to provide and add a little bit of color to how we did it. Would also like to position this as the customer was important and ultimately the hero for obtaining the value. This is going to Director level employees as high as Chief Operating Officer. I have attached a rough draft of the information we would like to convey but I am no designer. You will also find Use your expert design skills to think outside the box. Thank! Please contact me with any questions.

Walter

Target Market(s)

Industrial manufacturing, large commercial buildings (hospital, hotel, school, multifamily, assisted living), Director of Energy, CFO, COO

Industry/Entity Type

Drug Manufacturer

Font styles to use
Serif
Sans Serif

Requirements
Must have
• Clean, professional feel, ability to edit with adobe design software, ability to fit all key information.
Nice to have
• Redesigned graphic, clean printing.
Should not have
• Any childish themes

```html
<!DOCTYPE html>
<html lang="en">
<head>
<meta charset="utf-8">
<title>Keystride Energy – Case Study</title>
<link href="https://fonts.googleapis.com/css2?family=Oswald:wght@400;500;700&family=Open+Sans:wght@400;600;700&display=swap" rel="stylesheet">
<style>
  :root{
    --green:#8dc63f;
    --blue:#1f5c9c;
    --navy:#1d3a63;
    --gray:#6d6e71;
    --light-gray:#a7a9ac;
    --white:#ffffff;
  }
  *{margin:0;padding:0;box-sizing:border-box}
  html,body{width:849px;height:1200px;overflow:hidden;background:var(--white)}
  body{font-family:"Open Sans",Arial,sans-serif;color:var(--navy)}
  .sheet{position:relative;width:849px;height:1200px;overflow:hidden}

  /* header */
  .brand{position:absolute;left:26px;top:22px;display:flex;align-items:center;gap:10px}
  .brand-dot{width:30px;height:30px;border-radius:50%;background:var(--green)}
  .brand-name{font-weight:700;font-size:30px;color:var(--blue);line-height:1}
  .title-box{position:absolute;left:432px;top:10px;width:398px;height:54px;background:var(--green);border-radius:6px;
    font-weight:700;font-size:42px;color:var(--navy);text-align:center;line-height:54px}
  .subtitle{position:absolute;left:432px;top:70px;width:398px;text-align:center;font-size:21px;color:var(--gray)}

  /* section headings */
  .section-title{position:absolute;left:0;width:849px;text-align:center;font-family:"Oswald",Arial,sans-serif;font-weight:700;line-height:1;text-transform:uppercase}
  .rules-title{top:108px;font-size:62px;color:var(--gray)}
  .results-title{top:366px;font-size:62px;color:var(--blue)}
  .summary-title{top:818px;font-size:80px;color:var(--gray)}
  .connectors{position:absolute;left:0;top:0}

  /* rule boxes */
  .rule{position:absolute;top:188px;width:240px;height:148px;border:4px solid var(--green);
    display:flex;align-items:center;justify-content:center;text-align:center;
    font-family:"Oswald",Arial,sans-serif;font-weight:700;font-size:44px;line-height:1.02;text-transform:uppercase;padding:6px}
  .rule-green{color:var(--green)}
  .rule-gray{color:var(--gray)}
  .rule-caption{position:absolute;top:344px;width:240px;text-align:center;font-size:10.5px;color:var(--gray);text-transform:uppercase;line-height:1.3}

  /* results band */
  .results-band{position:absolute;left:0;top:447px;width:849px;height:360px;background:var(--blue);color:var(--white)}
  .result-col{position:absolute;top:56px;width:250px}
  .result-head{display:flex;align-items:center;gap:10px;font-size:25px;font-weight:600;margin-bottom:16px}
  .step-num{width:30px;height:30px;border-radius:50%;background:var(--green);color:var(--white);font-size:17px;font-weight:700;display:flex;align-items:center;justify-content:center}
  .result-list{list-style:none;padding-left:40px;font-size:15px;line-height:1.6;white-space:nowrap}
  .chart{position:absolute;left:300px;top:40px;width:250px;height:175px;background:var(--white)}

  /* summary */
  .facts{position:absolute;top:910px;width:330px;font-size:17px;line-height:1.2}
  .fact-label{font-weight:700;color:var(--navy)}
  .fact-value{color:var(--green);font-weight:600;margin-bottom:8px}
  .story{position:absolute;top:1034px;width:345px;font-size:13px;line-height:1.4;color:var(--blue)}

  /* footer */
  .footer{position:absolute;left:0;top:1106px;width:849px;height:94px;background:var(--blue);color:var(--white)}
  .footer-contact{position:absolute;left:30px;top:16px;font-size:14px;line-height:1.5}
  .footer-contact strong{font-weight:700}
  .footer-web{position:absolute;left:530px;top:18px;width:290px;height:56px;background:var(--white);color:var(--blue);padding:6px 14px;font-size:15px;line-height:1.45;font-weight:600}
</style>
</head>
<body>
<main class="sheet">

  <header>
    <div class="brand"><span class="brand-dot"></span><span class="brand-name">Keystride Energy</span></div>
    <div class="title-box">Case Study</div>
    <p class="subtitle">Energy Projects Save XYZ Money</p>
  </header>

  <svg class="connectors" width="849" height="460" aria-hidden="true">
    <g fill="none" stroke="#a7a9ac" stroke-width="3">
      <path d="M142 140 H40 V186"/>
      <path d="M707 140 H810 V186"/>
      <path d="M424 172 V186"/>
    </g>
    <g fill="none" stroke="#1f5c9c" stroke-width="3">
      <path d="M205 400 H40 V447"/>
      <path d="M644 400 H810 V447"/>
    </g>
  </svg>

  <h2 class="section-title rules-title">The Rules</h2>

  <div class="rule rule-green" style="left:22px">R ≠ NR +<br>AGS</div>
  <div class="rule rule-gray" style="left:304px">Patience<br>is not<br>a virtue</div>
  <div class="rule rule-green" style="left:588px">Resource<br>accoring<br>to value</div>
  <p class="rule-caption" style="left:22px">Owen Harlow, President XYZ</p>
  <p class="rule-caption" style="left:304px">Peter Lindqvist, VP Net XYZ</p>
  <p class="rule-caption" style="left:588px">Martin Cole, Previous Global Energy Manager XYZ</p>

  <h2 class="section-title results-title">The Results</h2>

  <section class="results-band">
    <div class="result-col" style="left:40px">
      <div class="result-head"><span class="step-num">1</span>Methodology</div>
      <ul class="result-list">
        <li>Rapid project replication</li>
        <li>Utilize system experts</li>
        <li>Leverage incentive funds</li>
        <li>Passionate skilled coaching</li>
      </ul>
    </div>

    <svg class="chart" viewBox="0 0 252 170" role="img" aria-label="Line chart of energy savings against target over time">
      <g stroke="#d9d9d9" stroke-width="1">
        <line x1="30" y1="20" x2="240" y2="20"/><line x1="30" y1="50" x2="240" y2="50"/>
        <line x1="30" y1="80" x2="240" y2="80"/><line x1="30" y1="110" x2="240" y2="110"/>
      </g>
      <line x1="30" y1="140" x2="240" y2="140" stroke="#6d6e71"/>
      <line x1="30" y1="12" x2="30" y2="140" stroke="#6d6e71"/>
      <polygon points="60,138 120,40 238,16 238,138" fill="#8dc63f" opacity="0.35"/>
      <polyline points="40,138 100,124 160,104 238,80" fill="none" stroke="#6d6e71" stroke-width="2"/>
      <polyline points="40,138 80,110 120,40 238,16" fill="none" stroke="#8dc63f" stroke-width="2.5"/>
      <rect x="40" y="22" width="8" height="4" fill="#8dc63f"/>
      <text x="52" y="27" font-size="7" fill="#6d6e71" font-family="Open Sans, sans-serif">Actual savings</text>
      <rect x="40" y="32" width="8" height="4" fill="#6d6e71"/>
      <text x="52" y="37" font-size="7" fill="#6d6e71" font-family="Open Sans, sans-serif">Target savings</text>
      <text x="150" y="132" font-size="7" fill="#6d6e71" font-family="Open Sans, sans-serif">Forecast</text>
      <g font-size="7" fill="#6d6e71" font-family="Open Sans, sans-serif" text-anchor="middle">
        <text x="40" y="152">2012</text><text x="90" y="152">2013</text><text x="140" y="152">2014</text><text x="190" y="152">2015</text><text x="236" y="152">2016</text>
      </g>
    </svg>

    <div class="result-col" style="left:590px">
      <div class="result-head"><span class="step-num">2</span>Optimization</div>
      <ul class="result-list">
        <li>Process Control</li>
        <li>Heat Recovery</li>
        <li>Major Equipment</li>
        <li>Data Management</li>
        <li>Fuels</li>
      </ul>
    </div>
  </section>

  <h2 class="section-title summary-title">Summary</h2>

  <div class="facts" style="left:80px">
    <p class="fact-label">Company:</p>
    <p class="fact-value">Fortune 100 Company</p>
    <p class="fact-label">Original Goal:</p>
    <p class="fact-value">15% reduction by 2020</p>
  </div>
  <div class="facts" style="left:478px">
    <p class="fact-label">Actual Results:</p>
    <p class="fact-value">17.3% reduction by 2015</p>
    <p class="fact-label">Additional Value Created:</p>
    <p class="fact-value">$240,000,000</p>
  </div>

  <p class="story" style="left:40px">The key to success was accelerating energy project approvals and pushing the time line to get those projects implemented. Achieving the corporate goal early led to</p>
  <p class="story" style="left:460px">remarkable cost performance. From 2012 to 2015 over 100 projects were completed and an addition 200 projects to the pipeline for 2015 – 2017.</p>

  <footer class="footer">
    <p class="footer-contact">For more information on exceeding energy goals:<br><strong>Martin Cole</strong>, Chief Operating Officer<br>(555) 555-5555 | martin@keystride.com</p>
    <p class="footer-web">Visit us online:<br>www.keystrideenergy.com</p>
  </footer>

</main>
</body>
</html>
```